STAND OUT BUSINESS CARD REQUIRED

I would like a business card that is going to be different and stand out!

Target Market(s)

Residential market, adults from 28yrs on

Industry/Entity Type

Electrician

Requirements
Must have
• Business name
• my name
• phone number
• email
• web address
• license no.
• abn
• fax no
• logo
Nice to have
• Extra info:
• FREE quotes
• Fixed pricing
• On time guarantee
• Life time labour Guarantee

```html
<!DOCTYPE html>
<html lang="en">
<head>
<meta charset="utf-8">
<title>Bright Spark Electrical – Business Cards</title>
<link href="https://fonts.googleapis.com/css2?family=Source+Sans+3:wght@400;700&display=swap" rel="stylesheet">
<style>
  :root {
    --stage: #050608;
    --white: #ffffff;
    --green: #189c47;
    --orange: #f28322;
    --bulb: #bfe6f6;
    --skin: #f6d5a8;
  }
  * { margin: 0; padding: 0; box-sizing: border-box; }
  html, body {
    width: 1200px; height: 1079px; overflow: hidden;
    background: var(--stage);
    font-family: "Source Sans 3", "Myriad Pro", Arial, sans-serif;
  }
  .sheet { position: relative; width: 1200px; height: 1079px; }
  .card {
    position: absolute; width: 517px; height: 287px; overflow: hidden;
  }
  .card--left { left: 72px; }
  .card--right { left: 607px; }
  .row-1 { top: 51px; }
  .row-2 { top: 392px; }
  .row-3 { top: 732px; }
  .bg-white { background: var(--white); }
  .bg-green { background: var(--green); }
  .bg-orange { background: var(--orange); }

  .mascot {
    position: absolute; border-radius: 46% 46% 40% 40%;
    background: radial-gradient(circle at 72% 22%, var(--bulb) 0 22%, transparent 23%),
                linear-gradient(160deg, var(--skin) 0%, var(--green) 70%);
    opacity: .85;
  }
  .front .mascot { left: 180px; top: 11px; width: 203px; height: 210px; }
  .back .mascot { left: 398px; top: 19px; width: 92px; height: 100px; }

  .brand-name {
    position: absolute; font-weight: 700; white-space: nowrap; letter-spacing: .5px;
  }
  .front .brand-name { left: 134px; top: 226px; font-size: 24px; }
  .back .brand-name { left: 372px; top: 124px; font-size: 12px; }

  .person { position: absolute; left: 56px; top: 106px; line-height: 1.05; }
  .person__name { font-size: 26px; }
  .person__role { font-size: 21px; padding-left: 15px; }

  .contact {
    position: absolute; left: 379px; top: 198px; list-style: none;
    font-size: 14px; line-height: 20px;
  }

  .t-white { color: var(--white); }
  .t-green { color: var(--green); }
  .t-orange { color: var(--orange); }
</style>
</head>
<body>
<main class="sheet">

  <!-- Row 1: white -->
  <section class="card card--left row-1 bg-white front">
    <div class="mascot" role="img" aria-label="Illustrated superhero electrician mascot holding a light bulb"></div>
    <p class="brand-name t-orange">Bright Spark Electrical</p>
  </section>
  <section class="card card--right row-1 bg-white back">
    <div class="person">
      <p class="person__name t-green">Your Name</p>
      <p class="person__role t-orange">occupation</p>
    </div>
    <div class="mascot" role="img" aria-label="Illustrated superhero electrician mascot holding a light bulb"></div>
    <p class="brand-name t-orange">Bright Spark Electrical</p>
    <ul class="contact">
      <li><span class="t-green">T.</span><span class="t-orange">0123456789</span></li>
      <li><span class="t-green">F.</span><span class="t-orange">0123456789</span></li>
      <li><span class="t-green">your</span><span class="t-orange">@your.com</span></li>
      <li class="t-green">www.your.com</li>
    </ul>
  </section>

  <!-- Row 2: orange / green -->
  <section class="card card--left row-2 bg-orange front">
    <div class="mascot" role="img" aria-label="Illustrated superhero electrician mascot holding a light bulb"></div>
    <p class="brand-name t-white">Bright Spark Electrical</p>
  </section>
  <section class="card card--right row-2 bg-green back">
    <div class="person">
      <p class="person__name t-orange">Your Name</p>
      <p class="person__role t-white">occupation</p>
    </div>
    <div class="mascot" role="img" aria-label="Illustrated superhero electrician mascot holding a light bulb"></div>
    <p class="brand-name t-orange">Bright Spark Electrical</p>
    <ul class="contact">
      <li><span class="t-orange">T.</span><span class="t-white">0123456789</span></li>
      <li><span class="t-orange">F.</span><span class="t-white">0123456789</span></li>
      <li><span class="t-orange">your</span><span class="t-white">@your.com</span></li>
      <li class="t-orange">www.your.com</li>
    </ul>
  </section>

  <!-- Row 3: green / orange -->
  <section class="card card--left row-3 bg-green front">
    <div class="mascot" role="img" aria-label="Illustrated superhero electrician mascot holding a light bulb"></div>
    <p class="brand-name t-orange">Bright Spark Electrical</p>
  </section>
  <section class="card card--right row-3 bg-orange back">
    <div class="person">
      <p class="person__name t-green">Your Name</p>
      <p class="person__role t-white">occupation</p>
    </div>
    <div class="mascot" role="img" aria-label="Illustrated superhero electrician mascot holding a light bulb"></div>
    <p class="brand-name t-white">Bright Spark Electrical</p>
    <ul class="contact">
      <li><span class="t-green">T.</span><span class="t-white">0123456789</span></li>
      <li><span class="t-green">F.</span><span class="t-white">0123456789</span></li>
      <li><span class="t-green">your</span><span class="t-white">@your.com</span></li>
      <li class="t-green">www.your.com</li>
    </ul>
  </section>

</main>
</body>
</html>
```